Corwell Holdings Business Cards

Hello. I need business cards designed with our new logo. I'd like to see at least 3 different designs. At least one with a dark background, and at least one with a white background. Maybe one with gray or blue for the background. Play with gradient colors and maybe even insert a pic of a skyline in the background of one or more of them. Use your judgement. We will need 2 cards printed. They need to accommodate the employee name, title, company address, phone, email, and website. Thanks.

Target Market(s)

Wealthy mature investors.

Contact Information for Business Card

Single-sided, professional, clean design that incorporates our logo.

Font styles to use
Sans Serif

Requirements
Must have
• Our new logo needs to be featured on it. (See attached.)
• Employee Name (In all CAPS)
• Title
• Street Address, City, ST Zip Code
• Cell Phone #, Email Address, Website Address
Nice to have
• Design that blends well with our new logo and its colors, or a city scape or other graphic design that looks like an apartment complex in the background. Blues and grays are nice, but use your judgement.
Should not have
• Modern or oriental looking designs or bright colors.

```html
<!DOCTYPE html>
<html lang="en">
<head>
<meta charset="utf-8">
<title>Corwell Holdings Business Card</title>
<link rel="stylesheet" href="https://fonts.googleapis.com/css2?family=Arimo:wght@400&display=swap">
<style>
  :root {
    --brand-blue: #29a8e0;
    --brand-gray: #6d6e71;
    --ink: #000000;
    --paper: #ffffff;
  }
  * { margin: 0; padding: 0; box-sizing: border-box; }
  html, body { width: 1200px; height: 601px; overflow: hidden; background: var(--paper); }
  .card {
    position: relative;
    width: 1200px;
    height: 601px;
    background: var(--paper);
    font-family: "Arimo", Arial, sans-serif;
    color: var(--ink);
  }
  .brand {
    position: absolute;
    left: 178px;
    top: 168px;
    height: 110px;
    display: flex;
    align-items: center;
    gap: 42px;
  }
  .brand-square {
    width: 110px;
    height: 110px;
    background: var(--brand-gray);
  }
  .brand-name {
    color: var(--brand-blue);
    font-size: 46px;
    font-weight: 400;
    line-height: 1;
    white-space: nowrap;
  }
  .employee {
    position: absolute;
    left: 22px;
    top: 390px;
    width: 583px;
  }
  .employee-name {
    font-size: 34px;
    font-weight: 400;
    letter-spacing: 1.5px;
    line-height: 1;
  }
  .employee-name .surname { color: var(--brand-blue); }
  .employee-title {
    font-size: 20px;
    letter-spacing: 0.8px;
    line-height: 1;
    margin-top: 9px;
    padding-bottom: 7px;
    border-bottom: 3px solid var(--ink);
  }
  .contact {
    list-style: none;
    margin-top: 3px;
    font-size: 23px;
    line-height: 29.5px;
    letter-spacing: 1.1px;
    white-space: nowrap;
  }
</style>
</head>
<body>
  <main class="card">
    <div class="brand">
      <div class="brand-square" aria-hidden="true"></div>
      <p class="brand-name">Corwell Holdings, LLC</p>
    </div>
    <section class="employee">
      <h1 class="employee-name">MARTIN <span class="surname">CORWELL</span></h1>
      <p class="employee-title">Principal (Manager) RM Heritage Partners, LLC</p>
      <ul class="contact">
        <li class="contact-phone">(555) 214-0388</li>
        <li class="contact-address">418 Brookline Ave Linden, Marlow, 75210, Texas</li>
        <li class="contact-email">martin@corwellholdings.com</li>
        <li class="contact-web">www.corwellresidential.com</li>
      </ul>
    </section>
  </main>
</body>
</html>
```